Business Card Design Project

Beauty Therapist
Bold, bright, feminine, like contrast, love flowers, girly stuff. Must be beautiful. But open to all suggestions. Business name: Plucky Plum.
xxx
Dorota Kaczmarczyk
Updates

Project Deadline Extended
Reason: I think you need more time to design something good. X

Target Market(s)

ignore this

Industry/Entity Type

Business

```html
<!DOCTYPE html>
<html lang="en">
<head>
<meta charset="utf-8">
<title>Plucky Plum – Business Card</title>
<link rel="stylesheet" href="https://fonts.googleapis.com/css2?family=Questrial&display=swap">
<style>
  :root {
    --magenta: #f01fc4;
    --magenta-deep: #c80fa0;
    --night: #120714;
    --plum: #3b0f42;
    --ink: #140a14;
    --white: #ffffff;
    --backdrop: #eceae8;
  }
  * { box-sizing: border-box; margin: 0; padding: 0; }
  html, body { width: 1200px; height: 1023px; overflow: hidden; }
  body {
    background: var(--backdrop);
    font-family: "Questrial", "Century Gothic", sans-serif;
    position: relative;
  }
  .card {
    position: absolute;
    left: 190px;
    width: 820px;
    height: 468px;
    overflow: hidden;
    box-shadow: 0 6px 18px rgba(0,0,0,0.18);
  }
  .card--front { top: 29px; background: linear-gradient(135deg, var(--night) 0%, var(--plum) 55%, var(--night) 100%); }
  .card--back { top: 526px; background: var(--magenta); }
  .card__shapes { position: absolute; inset: 0; width: 100%; height: 100%; }
  .brand {
    position: absolute;
    text-align: center;
  }
  .brand__name {
    font-size: 72px;
    letter-spacing: 1px;
    line-height: 1;
  }
  .brand__role {
    font-size: 17px;
    letter-spacing: 1px;
    margin-top: 6px;
    text-align: right;
  }
  .card--front .brand { left: 0; right: 0; top: 150px; }
  .card--front .brand__name { color: var(--magenta); }
  .card--front .brand__role { color: var(--white); width: 480px; margin-left: auto; margin-right: auto; }
  .card--back .brand { left: 40px; top: 280px; }
  .card--back .brand__name { color: var(--ink); font-size: 58px; }
  .card--back .brand__role { color: var(--ink); font-size: 14px; }
  .contact {
    position: absolute;
    left: 420px;
    top: 70px;
    padding-left: 26px;
    border-left: 1px solid rgba(20,10,20,0.35);
    color: var(--ink);
  }
  .contact__name { font-size: 22px; font-weight: 700; letter-spacing: 0.5px; margin-bottom: 12px; }
  .contact__row { display: flex; align-items: center; gap: 10px; font-size: 16px; margin-bottom: 7px; }
  .contact__icon { width: 18px; height: 18px; flex: none; }
</style>
</head>
<body>

<section class="card card--front">
  <svg class="card__shapes" viewBox="0 0 820 468" preserveAspectRatio="none" aria-hidden="true">
    <rect x="120" y="0" width="30" height="468" fill="#ffffff" opacity="0.03"/>
    <rect x="330" y="0" width="60" height="468" fill="#a02aa8" opacity="0.08"/>
    <rect x="560" y="0" width="24" height="468" fill="#ffffff" opacity="0.04"/>
    <rect x="690" y="0" width="70" height="468" fill="#a02aa8" opacity="0.07"/>
    <path d="M0,468 L0,430 C180,430 300,380 420,320 C540,260 650,300 820,240 L820,468 Z" fill="var(--magenta)"/>
  </svg>
  <div class="brand">
    <div class="brand__name">Plucky Plum</div>
    <div class="brand__role">Beauty Therapist</div>
  </div>
</section>

<section class="card card--back">
  <svg class="card__shapes" viewBox="0 0 820 468" preserveAspectRatio="none" aria-hidden="true">
    <path d="M560,468 C620,400 640,330 700,250 C750,180 780,90 820,60 L820,468 Z" fill="var(--ink)"/>
  </svg>
  <div class="brand">
    <div class="brand__name">Plucky Plum</div>
    <div class="brand__role">Beauty Therapist</div>
  </div>
  <div class="contact">
    <div class="contact__name">Dorota Kaczmarczyk</div>
    <div class="contact__row">
      <svg class="contact__icon" viewBox="0 0 18 18"><circle cx="9" cy="9" r="9" fill="var(--ink)"/><path d="M6,4.5 L7.6,4.5 L8.3,7 L7.2,7.9 C7.8,9.3 8.7,10.2 10.1,10.8 L11,9.7 L13.5,10.4 L13.5,12 C10,12.5 5.5,8 6,4.5 Z" fill="var(--magenta)"/></svg>
      <span>123.456.7890</span>
    </div>
    <div class="contact__row">
      <svg class="contact__icon" viewBox="0 0 18 18"><circle cx="9" cy="9" r="9" fill="var(--ink)"/><rect x="4.5" y="6" width="9" height="6.5" fill="none" stroke="var(--magenta)" stroke-width="1.2"/><path d="M4.5,6 L9,9.5 L13.5,6" fill="none" stroke="var(--magenta)" stroke-width="1.2"/></svg>
      <span>xxxxxxxxxx@email.com</span>
    </div>
    <div class="contact__row">
      <svg class="contact__icon" viewBox="0 0 18 18"><circle cx="9" cy="9" r="9" fill="var(--ink)"/><circle cx="9" cy="9" r="4.5" fill="none" stroke="var(--magenta)" stroke-width="1.1"/><path d="M4.5,9 H13.5 M9,4.5 C7,7 7,11 9,13.5 M9,4.5 C11,7 11,11 9,13.5" fill="none" stroke="var(--magenta)" stroke-width="1"/></svg>
      <span>www.yourwebsite.com</span>
    </div>
  </div>
</section>

</body>
</html>
```